Brochure Design Project

We are a consulting engineering company and need to have our current company brochure updated and made to look a lot more professional.

We provide design and documentation of electrical, lighting, mechanical, hydraulic, fire, services to architects, interior designers, building owners and managers.

We are launching an updated website shortly and want a print brochure to send to clients.

Attached is our current brochure for reference.
Updates

The recent projects section should be renamed to "Completed Projects". Space should be allowed for 8 projects. I have uploaded 7 of these images and a new image will follow shortly.

We would like to include an image for each of our company services. I have uploaded 9 new images:

1. Electrical
2. Mechanical
3. Communications
4. Fire
5. Security
6. Lighting
7. Hydraulics
8. Computer Suite
9. Building Assessments

Target Market(s)

Architects, Interior Designers, Consultants, Professionals

Industry/Entity Type

Building

Requirements
Must have
• Very professional look
Simple and easy to read layout
Similar look and feel to our new website which is soon to be launched : http://www.sitehaven.co.uk/rkm/
Examples of our recent projects - around 6 projects with 1 or 2 photos per project. Will upload these soon.
A3 size, double sided with centre fold
Should not have
• Bright colours
Any comics or similar

```html
<!DOCTYPE html>
<html lang="en">
<head>
<meta charset="utf-8">
<title>RKM Consulting Services – Brochure Spread</title>
<link rel="stylesheet" href="https://fonts.googleapis.com/css2?family=PT+Sans+Narrow:wght@400;700&family=Open+Sans:ital,wght@0,400;0,700;1,700&display=swap">
<style>
  :root{
    --page-bg:#ffffff;
    --panel:#1e1e1e;
    --panel-edge:#000000;
    --stripe-light:#c3c8cb;
    --stripe-mid:#5f6468;
    --text:#f2f2f2;
    --text-soft:#d9d9d9;
    --logo:#b9bcbe;
    --fold:#2c2c2c;
  }
  *{margin:0;padding:0;box-sizing:border-box}
  html,body{width:1200px;height:866px;overflow:hidden;background:var(--page-bg)}
  body{position:relative;font-family:"PT Sans Narrow",sans-serif;color:var(--text)}

  .spread{position:absolute;left:27px;top:27px;width:1146px;height:811px;background:var(--panel);border:2px solid var(--panel-edge);box-shadow:4px 5px 6px rgba(0,0,0,.35);overflow:hidden}
  .band{position:absolute}
  .band--light-left{left:0;top:0;width:24px;height:100%;background:var(--stripe-light)}
  .band--mid-left{left:24px;top:0;width:80px;height:100%;background:var(--stripe-mid)}
  .band--mid-top{left:843px;top:0;width:196px;height:280px;background:var(--stripe-mid)}
  .band--light-top{left:1039px;top:0;width:105px;height:280px;background:var(--stripe-light)}
  .band--mid-bottom{left:843px;top:762px;width:196px;height:47px;background:var(--stripe-mid)}
  .band--light-bottom{left:1039px;top:762px;width:105px;height:47px;background:var(--stripe-light)}
  .fold{position:absolute;left:570px;top:0;width:1px;height:100%;background:var(--fold)}

  .brand{position:absolute;color:var(--logo);font-family:"Open Sans",sans-serif;font-weight:400;line-height:1}
  .brand--small{left:124px;top:24px;font-size:40px;letter-spacing:-1px}
  .brand--small-sub{left:126px;top:68px;font-size:5px;letter-spacing:1.5px}
  .brand--large{left:597px;top:22px;font-size:62px;letter-spacing:-1px}
  .brand--large-sub{left:598px;top:87px;font-size:11px;letter-spacing:2.6px}

  .content{position:absolute;left:123px;top:96px;width:420px}
  .section-title{font-size:16px;font-weight:700;color:var(--text);margin:0 0 8px}
  .content p,.content li{font-size:7.6px;line-height:1.2;color:var(--text-soft)}
  .content p{margin-bottom:8px}
  .content ul{list-style:disc;margin:0 0 10px 34px}
  .services{display:flex;gap:0;margin:-2px 0 10px}
  .services ul{width:143px;margin-bottom:0}
  .ethics{margin-left:38px}
  .ethics p{margin:6px 0 5px}
  .ethics ul{margin-left:0;padding-left:0;list-style:none}
  .ethics li::before{content:"•";margin-right:7px}
  .lead-item{margin-left:38px;list-style:disc}

  .contact{position:absolute;left:123px;top:526px;width:420px}
  .contact .section-title{font-size:12px;padding-bottom:5px;border-bottom:1px solid #8d8d8d;margin-bottom:16px}
  .address{position:absolute;left:0;top:30px;width:140px;text-align:right;font-family:"Open Sans",sans-serif;font-size:8px;line-height:1.3}
  .address em{font-weight:700}
  .address dl{margin-top:10px;display:grid;grid-template-columns:auto auto;justify-content:end;column-gap:3px}
  .address dt{text-align:left}
  .address dd{text-align:left}
  .map{position:absolute;left:150px;top:28px;width:275px;height:185px;border:2px solid #d9d9d9;background:linear-gradient(135deg,#e9e5dd 0%,#e6e1d6 45%,#d8d4c9 100%)}
  .web{position:absolute;left:123px;top:766px;width:420px;text-align:center;font-family:"Open Sans",sans-serif;font-weight:700;font-size:14.5px;color:var(--text)}

  .quote{position:absolute;left:598px;top:289px;width:522px;text-align:center;font-weight:700;font-size:22.5px;line-height:1.1;color:var(--text)}
  .photo{position:absolute;left:598px;top:354px;width:520px;height:391px;background:radial-gradient(ellipse at 40% 40%,#f2f2f2 0%,#cfcfcf 45%,#8c8c8c 80%,#5a5a5a 100%)}
</style>
</head>
<body>
  <div class="spread">
    <div class="band band--light-left"></div>
    <div class="band band--mid-left"></div>
    <div class="band band--mid-top"></div>
    <div class="band band--light-top"></div>
    <div class="band band--mid-bottom"></div>
    <div class="band band--light-bottom"></div>
    <div class="fold"></div>

    <!-- Inside panel -->
    <div class="brand brand--small">rkm</div>
    <div class="brand brand--small-sub">Consulting Services Pty Ltd</div>

    <section class="content">
      <h2 class="section-title">About Us</h2>
      <p>RKM was formed in November 1998 and has evolved into one of Perth's leading building services consulting practices.</p>
      <p>Our award winning projects cover all states and territories of Australia demonstrating our depth of experience.</p>
      <p>We work with all sectors of the property, infrastructure, mining, oil and gas and construction industries delivering, complex, multidiscipline building services engineering solutions.</p>
      <p>Our client base includes national, state and local governments, developers, tenants, builders, architects, project managers, interior designers and property/portfolio managers.</p>
      <p>RKM provides design, documentation and contract administration services associated with:</p>
      <div class="services">
        <ul><li>Electrical</li><li>Mechanical</li><li>Communications</li><li>Fire</li><li>Security</li></ul>
        <ul><li>Lighting</li><li>Hydraulics</li><li>Computer Suite</li><li>Building Assessments</li></ul>
      </div>

      <h2 class="section-title">Objectives</h2>
      <p>To provide the optimum, cost effective, energy efficient design solutions using the latest technological innovations.</p>
      <p>Our team at RKM aspires to:</p>
      <ul>
        <li>Surpass client expectation</li>
        <li>Ensure client understanding of design concepts</li>
        <li>Ensure timely provision of design input allowing ample time for consideration and inclusion</li>
      </ul>

      <h2 class="section-title">Work Ethics</h2>
      <ul class="lead-list" style="margin-left:0">
        <li class="lead-item">To protect the engineering interests of our clients from initial involvement to the conclusion of each project</li>
      </ul>
      <div class="ethics">
        <p>To provide:</p>
        <ul>
          <li>A level of diligence, based on sound preparation that will ensure client satisfaction</li>
          <li>Innovation in design</li>
          <li>A service orientated and responsive approach</li>
          <li>Continual implementation across all aspects of each project</li>
          <li>A unique, detailed and focused approach to each project</li>
        </ul>
      </div>
    </section>

    <section class="contact">
      <h2 class="section-title">Contact Us</h2>
      <div class="address">
        <em>42 Carrow Lane<br>Eastbrook, Western Australia 6010</em>
        <dl>
          <dt>Phone</dt><dd>: 08 9555 0142</dd>
          <dt>Fax</dt><dd>: 08 9555 0178</dd>
          <dt>Email</dt><dd><em>: info@rkmconsulting.com.au</em></dd>
        </dl>
      </div>
      <div class="map" role="img" aria-label="Street map showing the office location"></div>
    </section>

    <div class="web">www.rkmconsulting.com.au</div>

    <!-- Cover panel -->
    <div class="brand brand--large">rkm</div>
    <div class="brand brand--large-sub">Consulting Services Pty Ltd</div>

    <blockquote class="quote">“Every project receives a level of dedication, commitment and service to ensure client expectations are exceeded”</blockquote>
    <div class="photo" role="img" aria-label="Photograph of rolled architectural blueprints lying on technical drawings"></div>
  </div>
</body>
</html>
```